Fat Loss Specialist Personal Training

I need a flyer which is of a high professional standard and looks to the customer that it represents my business as a quality company. I am a personal trainer who specialises in Fat Loss and want this to be the main focus of the flyer. My business is called Summit Sculpt. Please have a look at my website to see what I offer - www.summit-sculpt.co.uk . On the flyer I want it to show what I offer such as one to one PT, nutrition plans etc. A5 Size Flyer.

Target Market(s)

Women

Industry/Entity Type

Business

Font styles to use
Other font styles liked:
• Arial

Requirements
Must have
• Personal Training
• Fat Loss Specialist
• Summit Sculpt Logo on it (my business)
• My details needs to be on it -
• Contact number - 07493021568
• Email - dan@summit-sculpt.co.uk
Nice to have
• Motivating to the customer
• Well presented
• High quality flyer
• Friendly approach
• Follow the same colour scheme as my website
Should not have
• No swear words
• No blurry images / texts

```html
<!DOCTYPE html>
<html lang="en">
<head>
<meta charset="utf-8">
<title>Summit Sculpt – Fat Loss Specialist Personal Training</title>
<link href="https://fonts.googleapis.com/css2?family=Arimo:ital,wght@0,400;0,700;1,400;1,700&display=swap" rel="stylesheet">
<style>
  :root {
    --red: #e3161b;
    --red-dark: #b80f13;
    --black: #0b0b0b;
    --charcoal: #1e1e1e;
    --grey: #3a3a3a;
    --mid-grey: #8a8a8a;
    --light-grey: #cfcfcf;
    --paper: #ffffff;
    --text-dark: #222222;
  }
  * { margin: 0; padding: 0; box-sizing: border-box; }
  html, body { width: 900px; height: 1200px; overflow: hidden; background: var(--paper); }
  body { font-family: "Arimo", Arial, sans-serif; color: var(--text-dark); }

  .flyer { position: relative; width: 900px; height: 1200px; background: var(--black); overflow: hidden; }

  /* Header */
  .header { position: absolute; left: 0; top: 0; width: 900px; height: 120px; background: var(--paper); }
  .brand { position: absolute; left: 40px; top: 18px; display: flex; align-items: center; gap: 14px; }
  .brand-mark { width: 22px; height: 22px; background: var(--red); }
  .brand-name { font-size: 54px; font-weight: 700; color: var(--charcoal); letter-spacing: -1px; line-height: 1; }
  .brand-tagline { position: absolute; left: 250px; top: 84px; font-size: 19px; font-style: italic; color: var(--red); }
  .brand-tagline strong { color: var(--charcoal); font-weight: 700; }

  /* Hero photo */
  .hero-photo { position: absolute; left: 0; top: 120px; width: 900px; height: 430px;
    background: linear-gradient(160deg, #c9c4bd 0%, #9a8f84 40%, #5d5650 75%, #2c2a28 100%); }

  .hero-band { position: absolute; left: 0; top: 430px; width: 900px; height: 200px; }

  .consult-badge { position: absolute; left: 660px; top: 320px; width: 210px; height: 210px; border-radius: 50%;
    background: var(--red); border: 5px solid var(--paper); box-shadow: 0 6px 16px rgba(0,0,0,.45);
    color: var(--paper); text-align: center; display: flex; flex-direction: column; justify-content: center; }
  .consult-badge .line { font-size: 25px; font-weight: 700; line-height: 1.12; }
  .consult-badge .now { font-size: 50px; font-weight: 700; line-height: 1.05; margin-top: 4px; }

  /* Left service panel */
  .services { position: absolute; left: 30px; top: 575px; width: 400px; height: 400px; background: var(--paper); }
  .services-heading { position: absolute; left: -10px; top: 18px; width: 340px; height: 40px; background: var(--red);
    color: var(--paper); font-size: 24px; font-weight: 700; line-height: 40px; padding-left: 22px; letter-spacing: .5px; }
  .services-body { position: absolute; left: 24px; top: 84px; right: 20px; font-size: 19px; line-height: 1.35; }
  .services-body p { margin-bottom: 14px; }
  .services-body ul { list-style: none; margin-bottom: 14px; }
  .services-body li { padding-left: 20px; position: relative; }
  .services-body li::before { content: "›"; position: absolute; left: 2px; top: -1px; color: var(--red); font-weight: 700; }

  /* Right fat loss column */
  .fatloss { position: absolute; left: 470px; top: 618px; width: 400px; color: var(--paper); }
  .fatloss h2 { font-size: 58px; font-weight: 400; line-height: 1; letter-spacing: -1px; }
  .fatloss .sub { font-size: 29px; margin-top: 8px; }
  .fatloss .intro { font-size: 17px; line-height: 1.35; color: var(--light-grey); margin-top: 24px; }
  .fatloss .promise { font-size: 17px; font-weight: 700; font-style: italic; color: var(--red); text-align: center; margin-top: 22px; line-height: 1.3; }

  .web-bar { position: absolute; left: 450px; top: 985px; width: 450px; height: 50px; background: var(--red);
    color: var(--paper); font-size: 25px; font-weight: 700; line-height: 50px; padding-left: 28px; }

  /* Trainer panel */
  .trainer { position: absolute; left: 0; top: 1040px; width: 900px; height: 160px; }
  .trainer-photo { position: absolute; left: 40px; top: 0; width: 130px; height: 140px;
    background: linear-gradient(180deg, #7a6f67 0%, #3d4650 60%, #22272d 100%); border: 3px solid var(--paper); }
  .trainer-bio { position: absolute; left: 190px; top: 12px; width: 260px; font-size: 17px; font-style: italic; line-height: 1.35; color: var(--text-dark); }
  .trainer-bio strong { font-style: normal; }
  .contact { position: absolute; left: 510px; top: 60px; font-size: 22px; color: var(--text-dark); }
  .contact-row { display: flex; align-items: center; gap: 12px; margin-bottom: 8px; }
  .contact-row svg { width: 22px; height: 22px; fill: var(--charcoal); }
</style>
</head>
<body>
<div class="flyer">
  <header class="header">
    <div class="brand"><span class="brand-mark"></span><span class="brand-name">Summit Sculpt</span></div>
    <div class="brand-tagline">Fat Loss Specialist <strong>Personal Training</strong></div>
  </header>

  <div class="hero-photo" role="img" aria-label="Gym photo of a woman doing a press-up with a personal trainer coaching beside her"></div>

  <svg class="hero-band" viewBox="0 0 900 200" preserveAspectRatio="none" aria-hidden="true">
    <path d="M0 60 Q300 120 560 70 L900 0 L900 200 L0 200 Z" fill="#2a2a2a"/>
    <path d="M0 90 Q320 150 600 95 L900 40 L900 200 L0 200 Z" fill="#0b0b0b"/>
    <path d="M0 118 Q330 165 620 118 L900 72 L900 80 L620 128 Q330 175 0 128 Z" fill="#555555"/>
  </svg>

  <div class="consult-badge">
    <span class="line">Book a</span>
    <span class="line">FREE 30 minute</span>
    <span class="line">consultation</span>
    <span class="now">NOW!</span>
  </div>

  <section class="services">
    <h2 class="services-heading">PERSONAL TRAINING</h2>
    <div class="services-body">
      <p>Effective Results in Efficient Time.<br><strong>One to One- If you have a goal, we can achieve it.</strong></p>
      <ul>
        <li>100% attention,</li>
        <li>100% passion,</li>
        <li>100% commitment,</li>
        <li>100% Summit Sculpt</li>
      </ul>
      <p>Meal Plans, Supplement Guides, Discounted Memberships, all inclusive of our Personal Training Package.</p>
    </div>
  </section>

  <section class="fatloss">
    <h2>FAT LOSS</h2>
    <p class="sub">Get Lean, Burn Fat.</p>
    <p class="intro">One to One training - Personal Training is the way forward if you want quick, effective results. Here at Summit Sculpt, we put every ounce of passion into our clients where we achieve results in efficient time with the results effective.</p>
    <p class="promise">"I WILL GET YOU RESULTS,<br>YOU WILL GET YOUR SUMMIT SCULPT"</p>
  </section>

  <svg style="position:absolute;left:0;top:960px;width:900px;height:240px" viewBox="0 0 900 240" preserveAspectRatio="none" aria-hidden="true">
    <path d="M0 40 L420 40 Q450 40 470 70 L900 70 L900 240 L0 240 Z" fill="#ffffff"/>
    <path d="M560 240 Q760 170 900 150 L900 240 Z" fill="#bdbdbd"/>
  </svg>

  <div class="web-bar">www.summit-sculpt.co.uk</div>

  <section class="trainer">
    <div class="trainer-photo" role="img" aria-label="Portrait photo of personal trainer Dan Harlow"></div>
    <p class="trainer-bio">My name is <strong>DAN HARLOW</strong> and helping you achieve your goals, is my goal. We will do it together</p>
    <div class="contact">
      <div class="contact-row">
        <svg viewBox="0 0 24 24" aria-hidden="true"><path d="M6.6 10.8a15 15 0 0 0 6.6 6.6l2.2-2.2a1 1 0 0 1 1-.25 11.4 11.4 0 0 0 3.6.57 1 1 0 0 1 1 1V20a1 1 0 0 1-1 1A17 17 0 0 1 3 4a1 1 0 0 1 1-1h3.5a1 1 0 0 1 1 1c0 1.25.2 2.45.57 3.57a1 1 0 0 1-.25 1z"/></svg>
        <span>07493021568</span>
      </div>
      <div class="contact-row">
        <svg viewBox="0 0 24 24" aria-hidden="true"><path d="M2 5h20v14H2z M3.5 6.5 12 13l8.5-6.5" fill="none" stroke="#1e1e1e" stroke-width="2"/></svg>
        <span>dan@summit-sculpt.co.uk</span>
      </div>
    </div>
  </section>
</div>
</body>
</html>
```